Two Rollup Banners Promoting Trade Association

UPDATE: Please do not recycle the prior designs we've had. I am looking for creativity and a new look. Otherwise, I would use the prior designers to just update their work.
I need two 48"x79" Pull Up Retractable Banners Designed.
One promotes the benefits of membership in the Residential Capital Partners Forum. The second promotes RCPF's role in the affordable housing ecosystem.
The content for each is attached. I'm also providing examples of two banners we recently created for our 30th Anniversary as well as some photos of our members if you choose to use them (although it's not necessary - just providing them as an option).
The banners don't have to mimic the ones we did for our 30th Anniversary. I'm simply providing them as examples of designs that meet the look and feel of our brand.
I've also provided our brand guidelines and the specs for the banner.
Updates
All,
We are looking for clean, modern, streamlined designs. No clip art. No waves. Don’t bury the message in the graphics.
Please keep that in mind as you submit designs.
Look and feel
Each slider illustrates characteristics of the customer's brand and the style your logo design should communicate.

```html
<!DOCTYPE html>
<html lang="en">
<head>
<meta charset="utf-8">
<title>RCPF Rollup Banners</title>
<link href="https://fonts.googleapis.com/css2?family=Bebas+Neue&family=Poppins:wght@300;400;500;600&display=swap" rel="stylesheet">
<style>
:root{
  --orange:#f47b2a;
  --peach:#fdb48e;
  --blush:#fde4d8;
  --slate:#5b6670;
  --steel:#8fa5b4;
  --ink:#4a545d;
  --stage:#6b7680;
  --paper:#ffffff;
  --stat-warm:#fff3ec;
  --stat-cool:#eef4f9;
}
*{margin:0;padding:0;box-sizing:border-box}
html,body{width:1200px;height:1004px;overflow:hidden;background:var(--stage)}
body{position:relative;font-family:"Poppins",sans-serif;color:var(--ink)}
.banner{position:absolute;top:80px;width:513px;height:843px;background:var(--paper);overflow:hidden}
.banner--membership{left:77px}
.banner--impact{left:610px}
.abs{position:absolute}
.display{font-family:"Bebas Neue",sans-serif;line-height:1;letter-spacing:-.5px}
.orange{color:var(--orange)}
.slate{color:var(--slate)}

/* brand lockup */
.brand{position:absolute;left:127px;top:47px;height:50px;display:flex;align-items:center;gap:10px}
.brand__mark{width:40px;height:40px;background:var(--orange)}
.brand__abbr{font-family:"Bebas Neue",sans-serif;font-size:62px;line-height:1;color:var(--slate);padding-top:6px}
.brand__name{font-size:8.5px;line-height:10.5px;font-weight:500;text-transform:uppercase;letter-spacing:.6px;color:var(--steel);border-left:1px solid #d5dbe0;padding-left:8px;width:130px}

/* decorative geometry */
.quarter{position:absolute;background:var(--steel)}
.dot{position:absolute;border-radius:50%;background:#5f6b78}

/* headline */
.headline{position:absolute;left:0;width:100%;text-align:center;font-family:"Bebas Neue",sans-serif;line-height:1;letter-spacing:-.5px}

/* pillars */
.hub{position:absolute;left:166px;top:292px;width:182px;height:182px;border-radius:50%;background:var(--blush);box-shadow:0 0 0 9px #fef1eb}
.hub__text{position:absolute;left:0;top:62px;width:100%;text-align:center;font-family:"Bebas Neue",sans-serif;font-size:32px;line-height:29px;color:var(--slate)}
.pillar{position:absolute;text-align:center;font-size:15.5px;font-weight:300;line-height:19.5px;color:var(--ink)}
.pillar__title{font-size:18.5px;font-weight:500;line-height:22px}
.pillar__title--orange{color:var(--orange)}
.pillar__title--dark{color:#2f3840}
.icon{position:absolute;width:22px;height:22px}

/* community */
.photo{position:absolute;border-radius:6px}
.photo--warm{background:linear-gradient(135deg,#b58f72,#6a5a55)}
.photo--grey{background:linear-gradient(135deg,#7b7f86,#3e3f47)}
.photo--hall{background:linear-gradient(180deg,#c7c5c4,#6e6c70)}
.photo--table{background:linear-gradient(135deg,#8d6e63,#3d3b42)}
.stat-num{font-size:24px;font-weight:600;color:#2f3840;line-height:1}
.stat-label{font-size:17.5px;font-weight:300;line-height:21px;color:var(--ink)}
.cta{position:absolute}
.cta__head{font-family:"Bebas Neue",sans-serif;font-size:19px;color:#2f3840;line-height:1}
.cta__url{display:flex;align-items:center;gap:8px;margin-top:4px;font-size:16.5px;color:var(--ink)}

/* impact */
.feature-photo{position:absolute;left:28px;top:283px;width:202px;height:283px;background:linear-gradient(135deg,#e8e4df,#9a8e86 60%,#4f5661)}
.body-copy{font-size:15px;line-height:18.5px;color:#2f3840}
.stat-box{position:absolute;left:50px;width:166px;border-radius:6px;text-align:center}
.stat-box--warm{top:603px;height:96px;background:var(--stat-warm);border:1px solid var(--peach)}
.stat-box--cool{top:710px;height:96px;background:var(--stat-cool);border:1px solid var(--steel)}
.stat-box__num{font-family:"Bebas Neue",sans-serif;font-size:34px;line-height:1;margin-top:12px}
.stat-box__label{font-size:14.5px;font-weight:300;line-height:18px;color:var(--ink);margin-top:4px}
.divider{position:absolute;left:236px;top:612px;width:1px;height:202px;background:#d5dbe0}
.checks{position:absolute;left:253px;top:618px;list-style:none}
.checks li{position:relative;padding-left:17px;font-size:15px;font-weight:300;line-height:19px;color:#2f3840;margin-bottom:12px}
.checks svg{position:absolute;left:0;top:3px}
</style>
</head>
<body>

<!-- Banner 1: membership -->
<section class="banner banner--membership">
  <div class="brand">
    <span class="brand__mark"></span>
    <span class="brand__abbr">RCPF</span>
    <span class="brand__name">Residential Capital Partners Forum</span>
  </div>
  <div class="quarter" style="left:430px;top:13px;width:69px;height:69px;border-bottom-left-radius:100%"></div>

  <h1 class="headline" style="top:128px;font-size:50px"><span class="orange">LIHTC Investor</span> <span class="slate">Only</span></h1>
  <h1 class="headline slate" style="top:178px;font-size:50px">Community</h1>
  <div class="abs" style="left:52px;top:185px;width:57px;height:28px;background:var(--peach);border-radius:0 0 29px 29px"></div>

  <div class="abs" style="left:417px;top:233px;width:26px;height:29px;background:var(--peach);border-top-left-radius:100%"></div>
  <div class="dot" style="left:437px;top:256px;width:14px;height:14px"></div>
  <div class="dot" style="left:17px;top:464px;width:18px;height:18px"></div>
  <div class="abs" style="left:26px;top:474px;width:36px;height:40px;background:var(--peach);border-bottom-right-radius:100%;z-index:0"></div>

  <div class="hub"><div class="hub__text">Where<br>Investors</div></div>

  <svg class="icon" style="left:200px;top:238px" viewBox="0 0 24 24" aria-hidden="true"><path fill="var(--orange)" d="M12 3a6.5 6.5 0 0 0-4 11.6V17h8v-2.4A6.5 6.5 0 0 0 12 3zm-3 16h6v2H9z"/></svg>
  <div class="pillar" style="left:190px;top:256px;width:130px">
    <div class="pillar__title pillar__title--orange">Learn</div>Conferences<br>&amp; Webinars
  </div>

  <svg class="icon" style="left:120px;top:287px" viewBox="0 0 24 24" aria-hidden="true"><g stroke="var(--orange)" stroke-width="2"><line x1="4" y1="4" x2="20" y2="20"/><line x1="20" y1="4" x2="4" y2="20"/><line x1="12" y1="12" x2="12" y2="2"/></g><circle cx="12" cy="12" r="3.5" fill="var(--orange)"/><g fill="var(--orange)"><circle cx="4" cy="4" r="2.2"/><circle cx="20" cy="4" r="2.2"/><circle cx="4" cy="20" r="2.2"/><circle cx="20" cy="20" r="2.2"/></g></svg>
  <div class="pillar" style="left:64px;top:314px;width:130px">
    <div class="pillar__title pillar__title--dark">Network</div>Peer Groups<br>&amp; Forums
  </div>

  <svg class="icon" style="left:422px;top:303px" viewBox="0 0 24 24" aria-hidden="true"><path fill="none" stroke="var(--orange)" stroke-width="2.2" d="M10 5H4v15h15v-6"/><path fill="var(--orange)" d="M14 3l7 5-7 5V10c-4 0-6 1-8 4 0-5 3-8 8-8z"/></svg>
  <div class="pillar" style="left:327px;top:314px;width:120px">
    <div class="pillar__title pillar__title--dark">Share</div>Candid<br>Investor Only<br>Exchange
  </div>

  <svg class="icon" style="left:100px;top:411px" viewBox="0 0 24 24" aria-hidden="true"><path fill="var(--orange)" d="M3 8h5a2.5 2.5 0 1 1 4 0h5v5a2.5 2.5 0 1 1 0 4v4H3z"/></svg>
  <div class="pillar" style="left:99px;top:416px;width:130px">
    <div class="pillar__title pillar__title--orange">Shape</div>Industry<br>Standards &amp;<br>Best Practices
  </div>

  <svg class="icon" style="left:362px;top:411px" viewBox="0 0 24 24" aria-hidden="true"><path fill="var(--orange)" d="M11 22V12C6 12 4 9 4 5c5 0 7 3 7 6 0-5 3-8 9-8 0 5-3 9-8 9v10zM6 22h12v-2H6z"/></svg>
  <div class="pillar" style="left:246px;top:416px;width:160px">
    <div class="pillar__title pillar__title--orange">Grow</div>Professional<br>Development &amp;<br>Emerging Leaders<br>Program
  </div>

  <h2 class="abs display orange" style="left:28px;top:543px;font-size:35px;line-height:31px;font-weight:400">Our<br>Community</h2>
  <div class="abs" style="left:28px;top:622px">
    <div class="stat-num">60+</div>
    <div class="stat-label">Investor Firms</div>
  </div>

  <div class="photo photo--warm" style="left:26px;top:684px;width:134px;height:121px" role="img" aria-label="Member speaking at a conference podium"></div>
  <div class="photo photo--grey" style="left:170px;top:573px;width:176px;height:123px" role="img" aria-label="Two members in discussion at a panel table"></div>
  <div class="photo photo--hall" style="left:352px;top:573px;width:134px;height:73px" role="img" aria-label="Attendees seated in a conference hall"></div>
  <div class="photo photo--table" style="left:170px;top:706px;width:176px;height:99px" role="img" aria-label="Members networking around a round table"></div>

  <div class="abs" style="left:363px;top:663px">
    <div class="stat-num">1000+</div>
    <div class="stat-label">Industry<br>Professionals</div>
  </div>
  <div class="abs" style="left:494px;top:694px;width:40px;height:40px;border-radius:50%;background:var(--steel)"></div>

  <div class="cta" style="left:363px;top:758px">
    <div class="cta__head">Join Us Today</div>
    <div class="cta__url"><svg width="10" height="13" viewBox="0 0 10 13" aria-hidden="true"><path fill="var(--orange)" d="M0 0l10 7-4 1 3 4-2 1-3-4-4 3z"/></svg>RCPF.org</div>
  </div>
</section>

<!-- Banner 2: ecosystem impact -->
<section class="banner banner--impact">
  <div class="brand">
    <span class="brand__mark"></span>
    <span class="brand__abbr">RCPF</span>
    <span class="brand__name">Residential Capital Partners Forum</span>
  </div>
  <div class="abs" style="left:422px;top:84px;width:54px;height:46px;background:var(--peach);border-bottom-left-radius:100%"></div>
  <div class="dot" style="left:465px;top:72px;width:24px;height:24px"></div>

  <h1 class="headline" style="top:140px;font-size:46px"><span class="slate">Where</span> <span class="orange">LIHTC Investing</span></h1>
  <h1 class="headline" style="top:185px;font-size:46px"><span class="orange">Excellence</span> <span class="slate">Begins</span></h1>

  <div class="abs" style="left:164px;top:263px;width:53px;height:37px;background:var(--steel);border-top-right-radius:100%"></div>
  <div class="abs" style="left:217px;top:263px;width:90px;height:252px;background:var(--orange);border-radius:0 90px 90px 0"></div>
  <div class="abs" style="left:230px;top:451px;width:60px;height:64px;background:var(--peach);border-bottom-right-radius:60px"></div>
  <div class="abs" style="left:233px;top:516px;width:74px;height:64px;background:var(--steel);border-bottom-left-radius:100%"></div>
  <div class="feature-photo" role="img" aria-label="Smiling professional working on a laptop in a bright kitchen"></div>
  <div class="abs" style="left:49px;top:283px;width:40px;height:40px;border-radius:50%;background:var(--steel)"></div>

  <h2 class="abs display orange" style="left:327px;top:314px;font-size:48px">30 Years</h2>
  <h2 class="abs display slate" style="left:327px;top:361px;font-size:48px">Of Impact</h2>
  <p class="abs body-copy" style="left:327px;top:416px;width:180px">Industry-Adopted Standards in Underwriting, Asset Management, Risk Rating &amp; More</p>

  <div class="cta" style="left:327px;top:534px">
    <div class="cta__head">Join Us Today</div>
    <div class="cta__url"><svg width="10" height="13" viewBox="0 0 10 13" aria-hidden="true"><path fill="var(--orange)" d="M0 0l10 7-4 1 3 4-2 1-3-4-4 3z"/></svg>RCPF.org</div>
  </div>

  <div class="stat-box stat-box--warm">
    <div class="stat-box__num orange">4 Million</div>
    <div class="stat-box__label">Rental Homes<br>Created</div>
  </div>
  <div class="stat-box stat-box--cool">
    <div class="stat-box__num slate">9.28 Million</div>
    <div class="stat-box__label">Low-Income<br>Households Served</div>
  </div>
  <div class="divider"></div>

  <ul class="checks">
    <li><svg width="11" height="10" viewBox="0 0 11 10" aria-hidden="true"><path fill="none" stroke="var(--slate)" stroke-width="1.6" d="M1 5l3 3 6-7"/></svg>Setting Industry Standards<br>&amp; Best Practices</li>
    <li><svg width="11" height="10" viewBox="0 0 11 10" aria-hidden="true"><path fill="none" stroke="var(--slate)" stroke-width="1.6" d="M1 5l3 3 6-7"/></svg>Building Community<br>Through Candid Exchange</li>
    <li><svg width="11" height="10" viewBox="0 0 11 10" aria-hidden="true"><path fill="none" stroke="var(--slate)" stroke-width="1.6" d="M1 5l3 3 6-7"/></svg>Promoting the Investor<br>Perspective</li>
    <li><svg width="11" height="10" viewBox="0 0 11 10" aria-hidden="true"><path fill="none" stroke="var(--slate)" stroke-width="1.6" d="M1 5l3 3 6-7"/></svg>Fostering Collaboration<br>Across the Ecosystem</li>
  </ul>
</section>

</body>
</html>
```